Get me out of Jail business cards!!!!

I need business cards done for my business. I own a BailBonds and I get people out of jail!

Colors are red white and black

I need it to say on the card these details:

Rollin’ Free Bailbonds

452 S Kettering Ave
Millbrook, GA 31907

409-555-0172

Open 24/7

On the back of the card:

Must check in every Tuesday.

______/______/______ court date
____________________ time
You must know your court date at all times!

Marla Tisdell - owner
Rosalind Tisdell - agent
Denise Crandon - agent

Industry/Entity Type

Bail bonds

Contact Information for Business Card

Colors are red white and black I need it to say on the card these details: Rollin’ Free Bailbonds 452 S Kettering Ave Millbrook, GA 31907 409-555-0172 Open 24/7 On the back of the card: Must check in every Tuesday. ______/______/______ court date ____________________ time You must know your court date at all times! Marla Tisdell - owner Rosalind Tisdell - agent Denise Crandon - agent

Font styles to use
Serif
Sans Serif

Colors
EB3D1F
EC4F4E
F09395
F8D3D4
FCEDEE

Requirements
Must have
• I listed the must haves in the business card details
Nice to have
• Handcuffs or jail bars or a man in a black and white suit

```html
<!DOCTYPE html>
<html lang="en">
<head>
<meta charset="utf-8">
<title>Rollin’ Free Bailbonds – Business Cards</title>
<link href="https://fonts.googleapis.com/css2?family=Arimo:wght@400;700&display=swap" rel="stylesheet">
<style>
  :root{
    --red:#eb1c1c;
    --ink:#1f1f22;
    --charcoal:#232327;
    --grey:#6b6b6b;
    --paper:#ffffff;
    --bg:#e9e9ea;
  }
  *{box-sizing:border-box;margin:0;padding:0}
  html,body{width:1200px;height:801px;overflow:hidden}
  body{background:var(--bg);font-family:"Arimo",Arial,sans-serif;position:relative}

  .card{position:absolute;top:245px;width:540px;height:310px;border-bottom:5px solid var(--red);
        box-shadow:0 10px 24px rgba(0,0,0,.18);overflow:hidden}
  .card--front{left:40px;background:var(--paper)}
  .card--back{left:620px;background:var(--charcoal)}

  .brand{position:absolute;font-weight:400;letter-spacing:.5px;white-space:nowrap}

  /* front */
  .card--front .brand{right:28px;top:34px;font-size:32px;color:var(--ink)}
  .open{position:absolute;left:34px;top:118px;font-size:24px;color:var(--ink)}
  .open strong{color:var(--red);font-weight:700}
  .owner{position:absolute;left:40px;top:168px}
  .owner .name{font-size:18px;font-weight:700;color:var(--red)}
  .owner .role{font-size:13px;color:var(--grey);margin-top:2px}
  .phone{position:absolute;right:40px;top:180px;font-size:14px;color:var(--grey);display:flex;align-items:center;gap:6px}
  .rule{position:absolute;left:40px;right:40px;top:216px;height:1px;background:var(--grey)}
  .address{position:absolute;left:40px;top:228px;font-size:14px;line-height:20px;color:var(--grey)}

  /* back */
  .card--back .brand{left:50%;transform:translateX(-50%);top:16px;font-size:32px;color:#e6e6e6}
  .panel{position:absolute;left:24px;right:24px;top:64px;height:170px;background:var(--paper);border-radius:12px;overflow:hidden;color:var(--ink)}
  .panel .band{height:30px;background:var(--red);color:#fff;font-size:14px;display:flex;align-items:center;justify-content:center}
  .field{display:flex;justify-content:center;align-items:flex-end;gap:6px;margin-top:14px;font-size:14px}
  .blank{display:inline-block;border-bottom:1px solid var(--ink);height:14px}
  .notice{text-align:center;font-size:15px;margin-top:20px}
  .staff{position:absolute;left:24px;right:24px;bottom:18px;display:flex;justify-content:space-between;align-items:center}
  .staff .member .name{font-size:15px;font-weight:700;color:var(--red)}
  .staff .member .role{font-size:14px;color:#fff;margin-top:1px}
  .staff .divider{width:1px;height:34px;background:#cfcfcf}
</style>
</head>
<body>
  <section class="card card--front">
    <div class="brand">Rollin’ Free Bailbonds</div>
    <div class="open">Open <strong>24/7</strong></div>
    <div class="owner">
      <div class="name">Marla Tisdell</div>
      <div class="role">Owner</div>
    </div>
    <div class="phone">
      <svg width="14" height="14" viewBox="0 0 24 24" aria-hidden="true"><path fill="#eb1c1c" d="M6.6 10.8a15.1 15.1 0 0 0 6.6 6.6l2.2-2.2c.3-.3.7-.4 1-.2 1.1.4 2.3.6 3.6.6.6 0 1 .4 1 1V20c0 .6-.4 1-1 1A17 17 0 0 1 3 4c0-.6.4-1 1-1h3.5c.6 0 1 .4 1 1 0 1.3.2 2.5.6 3.6.1.3 0 .7-.2 1z"/></svg>
      409-555-0172
    </div>
    <div class="rule"></div>
    <div class="address">452 S Kettering Ave<br>Millbrook, GA 31907</div>
  </section>

  <section class="card card--back">
    <div class="brand">Rollin’ Free Bailbonds</div>
    <div class="panel">
      <div class="band">Must check in every Tuesday.</div>
      <div class="field"><span class="blank" style="width:60px"></span>/<span class="blank" style="width:60px"></span>/<span class="blank" style="width:60px"></span><span>court date</span></div>
      <div class="field"><span class="blank" style="width:200px"></span><span>time</span></div>
      <div class="notice">You must know your court date at all times!</div>
    </div>
    <div class="staff">
      <div class="member"><div class="name">Marla Tisdell</div><div class="role">Owner</div></div>
      <div class="divider"></div>
      <div class="member"><div class="name">Rosalind Tisdell</div><div class="role">Agent</div></div>
      <div class="divider"></div>
      <div class="member"><div class="name">Denise Crandon</div><div class="role">Agent</div></div>
    </div>
  </section>
</body>
</html>
```